"1" Pager Webdesign + HTML Creation

In this project we ask you to create a Veltrano (the registration form will be opened on a second page) web design with the content & structure described in the attached PDF. You are absolutely free in your choice of colors & design. There is also no company logo on this site as it will serve as a demo site for future clients where the design & content can be adjusted.
Once we agree on the design we also ask you to convert it into a simple html page.
The site is not a regular company website with services etc. --> the main idea is to give client the ability to launch a dedicated server (VPS) fully automatically in the background from the web gui. This server will have a software installed that allows phishing simulations to test employees security awareness.....so there should be some logical flow from top to bottom that leads to the user to launch the server. The company details/ressources etc. are not important and can be really kept very small. Main point of the site is to explain user what the steps he needs to go through to launch that virtual server...so launch button must be also kinda big...
See example I created (jpg) --> I am not designer. This is just to illustrate what I mean with logical "flow"....
As for pricing: I don't expect a fully functional html site & finished design for this price and I am willing to pay an extra bonus for finalizing the design/site as I know the details are time consuming. This bonus could be agreed upon project start and paid via zenvora. What I want are a few design examples that show that you understood what I need. Depending how much custom graphics need to be created we can discuss extra bonus/time required...
The site is not a regular company website with services etc. --> the main idea is to give client the ability to launch a dedicated server (VPS) fully automatically in the background from the web gui. This server will have a software installed that allows phishing simulations to test employees security awareness.....so there should be some logical flow from top to bottom that leads to the user to launch the server.... Added Thursday, August 11, 2016
Coding
Coded - Design and coding required
Number of Pages Required
2 page
Look and feel

```html
<!DOCTYPE html>
<html lang="en">
<head>
<meta charset="utf-8">
<title>Veltrano – Phishing Simulation Platform</title>
<link href="https://fonts.googleapis.com/css2?family=Montserrat:wght@400;600;700&family=Open+Sans:wght@400;600;700&display=swap" rel="stylesheet">
<style>
:root{
  --orange:#e8643c;
  --teal:#1bbc9b;
  --purple:#7a72b2;
  --blue:#2d8fdc;
  --dark:#2f3338;
  --text:#4a4f55;
  --muted:#8b9096;
  --line:#e3e5e8;
  --light:#f3f4f6;
  --white:#ffffff;
}
*{box-sizing:border-box;margin:0;padding:0}
html,body{width:1200px;height:5294px;overflow:hidden}
body{font-family:"Open Sans",Arial,sans-serif;color:var(--text);background:var(--white);position:relative}
h1,h2,h3,.nav,.btn,.tab{font-family:"Montserrat",Arial,sans-serif}
section,header,footer{position:absolute;left:0;width:1200px}
.btn{display:inline-block;background:var(--orange);color:var(--white);font-size:13px;font-weight:600;letter-spacing:1px;text-transform:uppercase;padding:12px 26px;border-radius:2px}

/* hero */
.hero{top:0;height:688px;background:linear-gradient(120deg,#6f7e8f 0%,#9aa6b2 45%,#56616e 100%)}
.hero-photo{position:absolute;inset:0;background:linear-gradient(100deg,rgba(40,50,62,.55),rgba(40,50,62,.15) 50%,rgba(40,50,62,.5))}
.topbar{position:absolute;top:0;left:0;width:1200px;height:110px;display:flex;align-items:center;padding:0 88px}
.brand{display:flex;align-items:center;gap:12px;color:var(--white);font-family:"Montserrat",sans-serif;font-weight:700;font-size:28px;letter-spacing:1px}
.brand-mark{width:40px;height:40px;border:3px solid var(--white)}
.nav{display:flex;gap:30px;margin-left:auto;margin-right:48px}
.nav a{color:var(--white);font-size:13px;font-weight:600;text-decoration:none;text-transform:uppercase}
.hero-body{position:absolute;top:270px;width:1200px;text-align:center;color:var(--white)}
.play{width:96px;height:96px;border:3px solid var(--white);border-radius:50%;margin:0 auto;display:flex;align-items:center;justify-content:center}
.hero-body h1{font-size:44px;font-weight:400;margin:44px 0 30px}
.start-now{position:absolute;top:596px;width:1200px;text-align:center;color:var(--white);font-family:"Montserrat",sans-serif;font-weight:700;font-size:18px;letter-spacing:1px}
.start-now i{display:block;width:8px;height:8px;border-radius:50%;background:var(--white);margin:16px auto 0}

/* intro */
.intro{top:688px;height:582px;text-align:center}
.intro h2{margin-top:75px;font-size:28px;font-weight:600;color:var(--dark);line-height:1.45}
.venn{position:absolute;top:840px;left:0}
.venn-block{position:absolute;top:940px;width:240px;font-size:13px;color:var(--muted);line-height:1.5}
.venn-block h3{font-family:"Open Sans",sans-serif;font-size:20px;font-weight:400;color:var(--dark);margin-bottom:6px}
.how{position:absolute;top:1175px;width:1200px;text-align:center;color:var(--orange);font-family:"Montserrat",sans-serif;font-weight:700;font-size:15px;letter-spacing:1px}
.how span{display:block;font-size:22px;line-height:1;margin-top:12px}

/* process */
.process{top:1270px;height:255px;background:linear-gradient(90deg,#56595e,#8c8f93 50%,#5b5e63)}
.process p{position:absolute;top:70px;width:1200px;text-align:center;color:var(--white);font-size:22px;line-height:1.55}
.tabs{top:1525px;height:54px;display:flex;border-top:1px solid var(--line);border-bottom:1px solid var(--line)}
.tab{flex:1;display:flex;align-items:center;justify-content:center;font-size:14px;font-weight:700;color:var(--dark);letter-spacing:1px;border-right:1px solid var(--line)}
.tab.active{background:var(--blue);color:var(--white);position:relative}
.tab.active:after{content:"";position:absolute;bottom:-10px;left:50%;margin-left:-10px;border:10px solid transparent;border-bottom:0;border-top-color:var(--blue)}
.step{top:1579px;height:556px}
.step-art{position:absolute;left:140px;top:50px;width:440px;height:450px;background:radial-gradient(circle at 50% 45%,#eef4f9,#f9fbfc 70%)}
.step-info{position:absolute;left:612px;top:70px;width:500px}
.step-info h3{font-size:30px;font-weight:600;color:var(--dark)}
.step-info .lead{font-size:15px;margin:6px 0 30px}
.check{display:flex;gap:18px;margin-bottom:28px;font-size:16px}
.check small{display:block;font-size:12px;color:var(--muted)}
.btn-grey{background:#d3d6da;color:var(--white);margin-top:6px;padding:12px 36px}

/* launch */
.launch{top:2135px;height:378px;background:linear-gradient(180deg,#3b9be6 0%,#56b0ef 55%,#eaf4fc 100%)}
.launch-art{position:absolute;inset:0}
.launch-row{position:absolute;top:0;height:378px;width:1200px;display:flex;justify-content:center;align-items:center;gap:230px}
.launch-word{font-family:"Montserrat",sans-serif;font-weight:700;font-size:52px;color:var(--white);letter-spacing:1px}

/* video */
.video{top:2513px;height:628px;text-align:center}
.video h2{margin-top:82px;font-size:28px;font-weight:600;color:var(--dark);line-height:1.5}
.video-frame{position:absolute;left:328px;top:180px;width:554px;height:384px;background:linear-gradient(180deg,#7f8a96 0%,#5f6873 85%,#c9ccd0 100%);display:flex;flex-direction:column;align-items:center;justify-content:center;color:var(--white)}
.video-frame .play{width:84px;height:84px}
.powered{margin-top:50px;font-size:13px}
.powered b{font-weight:700}

/* resources */
.resources{top:3141px;height:682px;background:var(--light);text-align:center}
.resources h2{margin-top:70px;font-size:28px;font-weight:400;color:var(--dark)}
.card{position:absolute;top:144px;width:412px;height:430px;background:var(--white);text-align:left}
.card-img{height:184px}
.card h3{font-family:"Open Sans",sans-serif;font-size:20px;font-weight:400;color:var(--dark);margin:30px 28px 10px}
.card p{margin:0 28px;font-size:12px;line-height:1.6;color:var(--muted)}
.card .btn{margin:20px 28px;font-size:11px;padding:10px 22px}

/* tiles */
.tiles{top:3823px;height:300px;display:flex}
.tile{flex:1;position:relative;display:flex;flex-direction:column;align-items:center;justify-content:center;color:var(--white);font-family:"Montserrat",sans-serif;font-weight:600;font-size:18px;text-align:center;line-height:1.3}
.tile .play{width:70px;height:70px;margin-bottom:18px}

/* cta */
.cta{top:4123px;height:159px;background:var(--orange);color:var(--white)}
.cta-text{position:absolute;left:150px;top:42px}
.cta h2{font-size:38px;font-weight:400;line-height:1}
.cta p{font-size:15px;font-weight:600;margin-top:8px}
.cta-btn{position:absolute;right:145px;top:52px;border:2px solid var(--white);padding:16px 30px;font-family:"Montserrat",sans-serif;font-size:14px;letter-spacing:1px}
.map{top:4282px;height:229px;background:linear-gradient(135deg,#e9e6df,#dfe3e6 60%,#e8e5dc)}

/* contact */
.contact{top:4511px;height:201px}
.info{position:absolute;top:50px;width:300px;text-align:center;font-size:14px;line-height:1.5;color:var(--muted)}
.info svg{display:block;margin:0 auto 14px}
.info strong{display:block;font-size:22px;font-weight:400;color:var(--dark)}
.info a{color:var(--orange)}
.divider{position:absolute;left:88px;right:88px;bottom:0;height:1px;background:var(--line)}
.ask{top:4712px;height:477px}
.ask h2{margin-top:42px;text-align:center;font-size:30px;font-weight:600;color:var(--dark)}
.field{position:absolute;height:40px;border:1px solid var(--line);font-size:13px;color:#b3b7bc;padding:10px 14px}
.submit{position:absolute;left:265px;top:385px;width:670px;height:38px;background:var(--orange);color:var(--white);font-family:"Montserrat",sans-serif;font-weight:700;font-size:13px;letter-spacing:1px;display:flex;align-items:center;justify-content:center}

/* footer */
.footer{top:5189px;height:105px;background:var(--dark);color:#a9adb2;font-size:14px}
.footer p{position:absolute;left:88px;top:42px}
.footer p span{color:var(--orange)}
.social{position:absolute;right:88px;top:34px;display:flex;gap:10px}
.social i{width:32px;height:32px;border:1px solid #777c82;border-radius:50%}
.to-top{position:absolute;right:30px;top:-52px;width:34px;height:34px;border-radius:50%;background:var(--orange);display:flex;align-items:center;justify-content:center}
</style>
</head>
<body>

<header class="hero">
  <div class="hero-photo" role="img" aria-label="Photo of three business people working together at a laptop"></div>
  <div class="topbar">
    <div class="brand"><span class="brand-mark"></span>VELTRANO</div>
    <nav class="nav"><a>Home</a><a>About us</a><a>How it works</a><a>Ressources</a><a>Contact us</a></nav>
    <span class="btn">Get started</span>
  </div>
  <div class="hero-body">
    <div class="play"><svg width="34" height="38" viewBox="0 0 34 38"><path d="M4 3 L31 19 L4 35 Z" fill="none" stroke="#fff" stroke-width="3"/></svg></div>
    <h1>In 10 Minutes from Start to Phish!</h1>
    <span class="btn">Watch the video</span>
  </div>
  <div class="start-now">START NOW<i></i></div>
</header>

<section class="intro">
  <h2>Build your best Human Phishing and<br>Malware Defense with us</h2>
</section>
<svg class="venn" width="1200" height="300" viewBox="0 0 1200 300">
  <path d="M510 30 A110 110 0 0 1 690 30" fill="none" stroke="#7a72b2" stroke-width="2"/>
  <path d="M505 30 l10 -2 -4 10" fill="none" stroke="#7a72b2" stroke-width="2"/>
  <path d="M510 240 A110 110 0 0 0 690 240" fill="none" stroke="#7a72b2" stroke-width="2"/>
  <path d="M695 240 l-10 2 4 -10" fill="none" stroke="#7a72b2" stroke-width="2"/>
  <circle cx="565" cy="135" r="88" fill="#1bbc9b"/>
  <circle cx="671" cy="135" r="88" fill="#7a72b2" opacity=".92"/>
  <circle cx="560" cy="110" r="18" fill="none" stroke="#fff" stroke-width="4"/>
  <path d="M573 123 l14 14" stroke="#fff" stroke-width="5" stroke-linecap="round"/>
  <path d="M660 138 v-8 q-12 -8 -12 -22 a23 23 0 0 1 46 0 q0 14 -12 22 v8 z" fill="none" stroke="#fff" stroke-width="4"/>
  <text x="565" y="176" text-anchor="middle" fill="#fff" font-family="Montserrat,sans-serif" font-size="13" font-weight="700">MEASURE</text>
  <text x="671" y="176" text-anchor="middle" fill="#fff" font-family="Montserrat,sans-serif" font-size="13" font-weight="700">TRAIN</text>
</svg>
<div class="venn-block" style="left:226px;text-align:right"><h3>Test your users</h3>Fully automated Spear Phishing, Malware, SmiShing, and USB attack Simulations.</div>
<div class="venn-block" style="left:784px"><h3>Train your users</h3>Choose among many interactive lessons, engaging training modules, tips, videos, games, quiz etc.</div>
<div class="how">HOW IT WORKS?<span>+</span></div>

<section class="process" role="img" aria-label="Photo of a desk with keyboard and notebook">
  <p>It's so easy. After registration you can launch a<br>virtualized server with a full scale testing and education<br>platform within minutes.</p>
  <svg width="1200" height="255" style="position:absolute;top:0;left:0">
    <g fill="none" stroke="#fff" stroke-width="2" stroke-dasharray="5 5">
      <path d="M210 100 H380"/><path d="M210 100 V240"/>
      <path d="M990 100 H820"/><path d="M990 100 V240"/>
    </g>
    <path d="M204 232 l6 10 6 -10 M984 232 l6 10 6 -10" fill="none" stroke="#fff" stroke-width="2"/>
  </svg>
</section>

<section class="tabs">
  <div class="tab active">STEP 1</div><div class="tab">STEP 2</div><div class="tab">STEP 3</div>
</section>

<section class="step">
  <div class="step-art" role="img" aria-label="Illustration of a businessman beside a signpost with red arrows and clouds"></div>
  <div class="step-info">
    <h3>Basic Settings</h3>
    <p class="lead">Choose Your Preferred Campaign Settings</p>
    <div class="check"><svg width="32" height="32"><circle cx="16" cy="16" r="14" fill="none" stroke="#2d8fdc" stroke-width="2"/><path d="M9 16 l5 5 9-10" fill="none" stroke="#2d8fdc" stroke-width="2"/></svg><div>Duration of campaign<small>up to 3 years</small></div></div>
    <div class="check"><svg width="32" height="32"><circle cx="16" cy="16" r="14" fill="none" stroke="#2d8fdc" stroke-width="2"/><path d="M9 16 l5 5 9-10" fill="none" stroke="#2d8fdc" stroke-width="2"/></svg><div>Number of employees to test/train</div></div>
    <div class="check"><svg width="32" height="32"><circle cx="16" cy="16" r="14" fill="none" stroke="#2d8fdc" stroke-width="2"/><path d="M9 16 l5 5 9-10" fill="none" stroke="#2d8fdc" stroke-width="2"/></svg><div>Technical details<small>Domain names etc.</small></div></div>
    <div class="check"><svg width="32" height="32"><circle cx="16" cy="16" r="14" fill="none" stroke="#2d8fdc" stroke-width="2"/><path d="M9 16 l5 5 9-10" fill="none" stroke="#2d8fdc" stroke-width="2"/></svg><div>Choose additional services<small>Campaign setup support etc.</small></div></div>
    <span class="btn btn-grey">Explore more</span>
  </div>
</section>

<section class="launch">
  <div class="launch-art" role="img" aria-label="Illustration of a red rocket taking off above white clouds"></div>
  <div class="launch-row">
    <span class="launch-word">LAUNCH</span>
    <span class="launch-word">SERVER</span>
  </div>
</section>

<section class="video">
  <h2>Launch Your Virtualized Security Awareness<br>Training and Phishing/Malware Simulation Platform</h2>
  <div class="video-frame" role="img" aria-label="Laptop showing a video still of a team meeting">
    <div class="play"><svg width="30" height="34" viewBox="0 0 30 34"><path d="M4 3 L27 17 L4 31 Z" fill="none" stroke="#fff" stroke-width="3"/></svg></div>
    <p class="powered">Powered by <b>Nexa</b></p>
  </div>
</section>

<section class="resources">
  <h2>Ressources</h2>
  <article class="card" style="left:176px">
    <div class="card-img" role="img" aria-label="Photo of a hand touching a digital network interface" style="background:linear-gradient(120deg,#1f3d63,#5a86b5)"></div>
    <h3>Our Services</h3>
    <p>when an unknown printer took a galley of type and scrambled it to make a type specimen book. It has survived not only five centuries, but also the leap into electronic typesetting, remaining essentially unchanged.</p>
    <span class="btn">&#8681; About us PDF</span>
  </article>
  <article class="card" style="left:612px">
    <div class="card-img" role="img" aria-label="Photo of business people in an office" style="background:linear-gradient(120deg,#7c8795,#c2c8cf)"></div>
    <h3>About US</h3>
    <p>when an unknown printer took a galley of type and scrambled it to make a type specimen book. It has survived not only five centuries, but also the leap into electronic typesetting, remaining essentially unchanged.</p>
    <span class="btn">&#8681; About us PDF</span>
  </article>
</section>

<section class="tiles">
  <div class="tile" role="img" aria-label="Photo of two business people at a desk" style="background:linear-gradient(135deg,#4c5561,#78818b)"><div class="play"><svg width="24" height="26"><path d="M3 2 L21 13 L3 24 Z" fill="none" stroke="#fff" stroke-width="2"/></svg></div>Sample Campaign Wizard<br>Dummy Text</div>
  <div class="tile" role="img" aria-label="Photo of office skyscrapers" style="background:linear-gradient(135deg,#5a636d,#8c949c)"><div class="play"><svg width="24" height="26"><path d="M3 2 L21 13 L3 24 Z" fill="none" stroke="#fff" stroke-width="2"/></svg></div>Sample Campaign Wizard<br>Dummy Text</div>
  <div class="tile" role="img" aria-label="Photo of a business handshake" style="background:linear-gradient(135deg,#6a727b,#454c55)"><div class="play"><svg width="24" height="26"><path d="M3 2 L21 13 L3 24 Z" fill="none" stroke="#fff" stroke-width="2"/></svg></div>Sample Campaign Wizard<br>Dummy Text</div>
</section>

<section class="cta">
  <svg style="position:absolute;left:88px;top:48px" width="54" height="54" viewBox="0 0 54 54"><circle cx="20" cy="16" r="11" fill="none" stroke="#fff" stroke-width="3"/><path d="M2 50 q0-20 18-20 q18 0 18 20" fill="none" stroke="#fff" stroke-width="3"/><path d="M44 14 v16 M36 22 h16" stroke="#fff" stroke-width="3"/></svg>
  <div class="cta-text"><h2>Get Strated Now!</h2><p>Please register here and start your awareness program right away.</p></div>
  <span class="cta-btn">REGISTER NOW!</span>
</section>

<section class="map" role="img" aria-label="Street map of the office location with a red pin">
  <svg width="1200" height="229" style="position:absolute;top:0;left:0"><path d="M598 90 a12 12 0 1 1 24 0 c0 12 -12 24 -12 24 s-12 -12 -12 -24z" fill="#e8643c"/></svg>
</section>

<section class="contact">
  <div class="info" style="left:150px"><svg width="36" height="36"><path d="M18 4 v28 M6 8 h22 l4 4 -4 4 h-22 z" fill="none" stroke="#8b9096" stroke-width="2"/></svg>165 Dummy Street, Area Name<br>Lorem City, LM 1VJ17</div>
  <div class="info" style="left:450px"><svg width="36" height="36"><path d="M10 4 h8 l3 8 -5 4 q3 7 10 10 l4 -5 8 3 v8 q-22 2 -28 -28z" fill="none" stroke="#8b9096" stroke-width="2"/></svg><strong>1 - 800 - 555 - 0142</strong>support@veltrano.test</div>
  <div class="info" style="left:750px"><svg width="36" height="36"><circle cx="18" cy="18" r="15" fill="none" stroke="#8b9096" stroke-width="2"/><circle cx="18" cy="18" r="7" fill="none" stroke="#8b9096" stroke-width="2"/></svg>Need Help or Support?<br><a>Contact Us</a></div>
  <div class="divider"></div>
</section>

<section class="ask">
  <h2>Have a Question?</h2>
  <div class="field" style="left:265px;top:112px;width:326px">Name</div>
  <div class="field" style="left:609px;top:112px;width:326px">Email</div>
  <div class="field" style="left:265px;top:166px;width:326px">Phone</div>
  <div class="field" style="left:609px;top:166px;width:326px">Category <span style="float:right">&#9662;</span></div>
  <div class="field" style="left:265px;top:220px;width:670px;height:140px">Message</div>
  <div class="submit">SUBMIT</div>
</section>

<footer class="footer">
  <div class="to-top"><svg width="14" height="10"><path d="M1 9 L7 2 L13 9" fill="none" stroke="#fff" stroke-width="2"/></svg></div>
  <p><span>Veltrano</span> © 2016. All Right Reserved <span>Terms of Use</span> and <span>Privacy Policy</span></p>
  <div class="social"><i></i><i></i><i></i><i></i></div>
</footer>

</body>
</html>
```